Marnie Lux Business Card Design

I need a business card for my daughter. She has it all described in the file below. But it needs to be square in shape. http://www.marnielux.com is her web site

Target Market(s)

18-35 year old women

Industry/Entity Type

Fashion

Contact Information for Business Card

Please look at the attached file as it has all the details.

Requirements
Must have
• Please look at the attached file as it has all the details.
Nice to have
Should not have

```html
<!DOCTYPE html>
<html lang="en">
<head>
<meta charset="utf-8">
<title>Marnie Lux Business Card</title>
<link rel="stylesheet" href="https://fonts.googleapis.com/css2?family=Open+Sans:wght@400&family=Playfair+Display:wght@700&family=Bodoni+Moda:wght@500&family=Satisfy&display=swap">
<style>
  :root {
    --backdrop: #ece6e2;
    --ink: #000000;
    --blush: #f7d9de;
    --blush-text: #f5d3d6;
    --marble-dark: #0b0b0b;
    --marble-mid: #262626;
    --white: #ffffff;
    --body-text: #151515;
  }
  * { box-sizing: border-box; margin: 0; padding: 0; }
  html, body { width: 1200px; height: 1000px; overflow: hidden; }
  body { background: var(--backdrop); position: relative; font-family: "Open Sans", sans-serif; }

  .card { position: absolute; top: 252px; width: 495px; height: 495px; }

  /* Back side: contact details */
  .card-back { left: 73px; background: var(--ink); padding: 12px; }
  .card-back__face { position: relative; width: 100%; height: 100%; background: var(--blush); }
  .tagline-bar {
    position: absolute; left: 51px; top: 70px; width: 367px; height: 50px;
    background: var(--ink); color: var(--white);
    font-family: "Satisfy", cursive; font-size: 19px;
    display: flex; align-items: center; justify-content: center; white-space: nowrap;
  }
  .contact-list { position: absolute; left: 0; right: 0; top: 176px; list-style: none; text-align: center; }
  .contact-list li {
    height: 35.5px; display: flex; align-items: center; justify-content: center; gap: 8px;
    font-size: 17px; color: var(--body-text);
  }
  .contact-list .marker { width: 14px; height: 14px; background: var(--ink); border-radius: 50%; }
  .contact-list .marker--square { border-radius: 2px; }
  .contact-list svg { width: 16px; height: 12px; }
  .link-list { position: absolute; left: 0; right: 0; top: 334px; list-style: none; }
  .link-list li {
    height: 38px; display: flex; align-items: center; justify-content: center; gap: 4px;
    font-size: 17px; color: var(--body-text);
  }
  .link-list .label { font-family: "Playfair Display", serif; font-weight: 700; font-size: 15px; color: var(--white); }

  /* Front side: name */
  .card-front { left: 627px; overflow: hidden; }
  .marble {
    position: absolute; inset: 0;
    background:
      radial-gradient(ellipse at 80% 60%, var(--marble-mid) 0%, transparent 55%),
      radial-gradient(ellipse at 15% 20%, #1d1d1d 0%, transparent 50%),
      var(--marble-dark);
  }
  .brand-name {
    position: absolute; left: 0; right: 0; top: 186px; text-align: center;
    font-family: "Bodoni Moda", serif; font-weight: 500; font-size: 46px;
    letter-spacing: 5px; color: var(--blush-text);
  }
  .brand-slogan {
    position: absolute; left: 0; right: 0; top: 264px; text-align: center;
    font-family: "Satisfy", cursive; font-size: 28px; letter-spacing: 1px; color: var(--blush-text);
  }
</style>
</head>
<body>
  <section class="card card-back" aria-label="Card back with contact details">
    <div class="card-back__face">
      <div class="tagline-bar">blogger &amp; vlogger // Beauty - fashion - travel</div>
      <ul class="contact-list">
        <li><span class="marker marker--square"></span>picgram.com/marnieluxxo</li>
        <li><span class="marker"></span>chirper.com/marnieluxxo</li>
        <li><span class="marker"></span>@marnieluxxo</li>
        <li>
          <svg viewBox="0 0 16 12" aria-hidden="true"><rect x="0" y="0" width="16" height="12" rx="1.5" fill="#000"/><path d="M1 1.5 L8 7 L15 1.5" stroke="#f7d9de" stroke-width="1.6" fill="none"/></svg>
          marnie@marnielux.com
        </li>
      </ul>
      <ul class="link-list">
        <li><span class="label">BLOG:</span>marnielux.com</li>
        <li><span class="label">VIDTUBE:</span>vidtube.com/marnielux</li>
      </ul>
    </div>
  </section>

  <section class="card card-front" aria-label="Card front with name">
    <div class="marble" role="img" aria-label="Black marble texture with white veins"></div>
    <h1 class="brand-name">MARNIE LUX</h1>
    <p class="brand-slogan">dressed in daydreams</p>
  </section>
</body>
</html>
```